Linked In Profile Banner Needed

I am in need of a Linked In Banner photo for my profile. The dimensions are 1584 x 396 pixels and the bottom left is where Linked In places my photo over so be aware of that. I attached an example for your reference.

I have also attached my logo and business card so you can keep the same color & style conistant.

Also add the following text:

"Preserve capital with a tax advantaged lease for equipment, vehicles, software and more! $5,000 - $50m"

You can also look at our website here:
www.HarlowfieldFundingCo.com

```html
<!DOCTYPE html>
<html lang="en">
<head>
<meta charset="utf-8">
<title>Harlowfield Funding Co – Profile Banner</title>
<link rel="stylesheet" href="https://fonts.googleapis.com/css2?family=Cabin:ital,wght@0,400;1,400&display=swap">
<style>
  :root {
    --page: #f4f5f7;
    --banner-navy: #282944;
    --accent-cyan: #4cc4ea;
    --name-white: #f3f5fa;
    --band-top: #2f5878;
    --band-bottom: #2c396c;
    --bar-top: #3fc8f0;
    --bar-bottom: #3c58b4;
    --frame-white: #ffffff;
    --photo-light: #8a8d95;
    --photo-dark: #25262b;
  }
  * { margin: 0; padding: 0; box-sizing: border-box; }
  html, body {
    width: 1200px;
    height: 1200px;
    overflow: hidden;
    background: var(--page);
  }
  .canvas {
    position: relative;
    width: 1200px;
    height: 1200px;
  }
  .profile-banner {
    position: absolute;
    left: 40px;
    top: 460px;
    width: 1120px;
    height: 280px;
    background: var(--banner-navy);
    overflow: hidden;
    box-shadow: 0 18px 30px rgba(0, 0, 0, 0.22);
  }
  .skyline-band {
    position: absolute;
    bottom: 0;
    background: linear-gradient(180deg, var(--band-top) 0%, var(--band-bottom) 100%);
    opacity: 0.9;
  }
  .skyline-band--one { left: 0; width: 43px; height: 185px; }
  .skyline-band--two { left: 58px; width: 42px; height: 210px; }
  .skyline-band--three { left: 128px; width: 99px; height: 150px; border-right: 3px solid #5a6386; }
  .brand-name {
    position: absolute;
    right: 254px;
    top: 62px;
    display: flex;
    align-items: center;
    gap: 12px;
    font-family: "Cabin", sans-serif;
    font-weight: 400;
    font-size: 24px;
    letter-spacing: 1px;
    color: var(--name-white);
    white-space: nowrap;
  }
  .brand-mark {
    width: 22px;
    height: 22px;
    background: var(--accent-cyan);
  }
  .offer {
    position: absolute;
    right: 254px;
    top: 126px;
    text-align: right;
    font-family: "Cabin", sans-serif;
    font-style: italic;
    color: var(--accent-cyan);
  }
  .offer-line {
    font-size: 22.5px;
    line-height: 26px;
    white-space: nowrap;
  }
  .offer-range {
    font-size: 27px;
    line-height: 36px;
    letter-spacing: -1px;
    margin-top: 2px;
  }
  .accent-bar {
    position: absolute;
    background: linear-gradient(180deg, var(--bar-top) 0%, var(--bar-bottom) 100%);
  }
  .accent-bar--front {
    left: 885px;
    top: 65px;
    width: 44px;
    height: 194px;
    border-left: 4px solid var(--frame-white);
    border-bottom: 4px solid var(--frame-white);
  }
  .accent-bar--back {
    left: 943px;
    top: 40px;
    width: 40px;
    height: 130px;
  }
  .accent-bar--side {
    left: 1104px;
    top: 140px;
    width: 8px;
    height: 45px;
  }
  .portrait {
    position: absolute;
    left: 927px;
    top: 23px;
    width: 177px;
    height: 241px;
    background: linear-gradient(180deg, var(--photo-light) 0%, #55575e 45%, var(--photo-dark) 100%);
  }
</style>
</head>
<body>
  <main class="canvas">
    <section class="profile-banner">
      <div class="skyline-band skyline-band--one"></div>
      <div class="skyline-band skyline-band--two"></div>
      <div class="skyline-band skyline-band--three"></div>

      <div class="brand-name"><span class="brand-mark"></span>HARLOWFIELD FUNDING CO</div>
      <div class="offer">
        <p class="offer-line">Preserve capital with a tax advantaged lease for</p>
        <p class="offer-line">equipment, vehicles, software and more!</p>
        <p class="offer-range">$5,000 - $50m</p>
      </div>

      <div class="accent-bar accent-bar--front"></div>
      <div class="accent-bar accent-bar--back"></div>
      <div class="accent-bar accent-bar--side"></div>
      <div class="portrait" role="img" aria-label="Black and white portrait photo of the business owner in a suit with arms crossed"></div>
    </section>
  </main>
</body>
</html>
```